Stationery & Envelope Design

Executive Style looking stationery & envelope design.
Business Information:
Larkspur Ridge Homes
7385 Brindle Hollow Lane, Fairmont, OR 97402-2049
Phone: 541.555.0142
Fax: 541.555.0187

Industry/Entity Type

Business

```html
<!DOCTYPE html>
<html lang="en">
<head>
<meta charset="utf-8">
<title>Larkspur Ridge Homes – Stationery</title>
<link href="https://fonts.googleapis.com/css2?family=Arimo:wght@400;700&display=swap" rel="stylesheet">
<style>
  :root{
    --navy:#1d3f7a;
    --green:#7a8c35;
    --blue:#0a52a0;
    --ink:#2a2a2a;
    --grey:#555;
    --paper:#ffffff;
    --stage:#e9e6e1;
    --edge:#b9b9b9;
  }
  *{box-sizing:border-box;margin:0;padding:0}
  html,body{width:1200px;height:1071px;overflow:hidden}
  body{background:var(--stage);font-family:"Arimo",Arial,sans-serif;position:relative;color:var(--ink)}

  .sheet{position:absolute;top:40px;width:463px;height:599px;background:var(--paper);border:1px solid var(--edge);overflow:hidden}
  .sheet--fax{left:91px}
  .sheet--letter{left:640px}

  .brand{position:absolute;left:0;right:0;text-align:center;font-weight:400;font-size:17px;color:var(--navy);white-space:nowrap}
  .sheet .brand{top:62px}

  .fax-title{position:absolute;left:34px;top:126px;font-size:28px;font-weight:400;line-height:32px}
  .fax-field{position:absolute;left:38px;width:386px;height:20px;border-bottom:2px solid #333}
  .fax-field--to{top:189px}
  .fax-field--fax{top:242px}
  .fax-field--phone{top:296px}
  .fax-field--re{top:351px}
  .fax-label{position:absolute;top:0;font-size:11px;line-height:12px}
  .fax-label--right{left:251px}

  .chevron{position:absolute;left:0;bottom:0;width:100%;height:56px}
  .footer{position:absolute;bottom:6px;font-size:7.5px;color:var(--grey);line-height:1.4;white-space:nowrap}
  .footer--fax{left:145px;display:flex;gap:6px}
  .footer--fax .divider{width:1px;background:#999}
  .footer--letter{left:0;right:0;text-align:center}

  .env{position:absolute;width:517px;height:224px;background:var(--paper);border:1px solid var(--edge);overflow:hidden}
  .env__flap{position:absolute;left:0;top:0;width:100%;height:72px}
  .env .brand{top:24px;font-size:16px}
  .env--back1{left:87px;top:665px}
  .env--back2{left:57px;top:735px}
  .env--front{left:43px;top:811px}
  .env--green{left:621px;top:658px}
  .env--blue{left:605px;top:727px}
  .env--white{left:640px;top:806px}
  .env--front .brand{top:40px;left:12px;right:auto;text-align:left;font-size:14px}
  .brand--light{color:#fff}
  .brand--grey{color:#4a4a4a}
  .brand--black{color:#111}
  .env__address{position:absolute;bottom:8px;left:0;right:0;text-align:center;font-size:7.5px;color:var(--grey)}
</style>
</head>
<body>

<section class="sheet sheet--fax">
  <div class="brand">Larkspur Ridge Homes</div>
  <h1 class="fax-title">FAX</h1>
  <div class="fax-field fax-field--to"><span class="fax-label">To</span><span class="fax-label fax-label--right">From</span></div>
  <div class="fax-field fax-field--fax"><span class="fax-label">Fax</span><span class="fax-label fax-label--right">Pages</span></div>
  <div class="fax-field fax-field--phone"><span class="fax-label">Phone</span><span class="fax-label fax-label--right">Date</span></div>
  <div class="fax-field fax-field--re"><span class="fax-label">Re</span><span class="fax-label fax-label--right">CC</span></div>
  <svg class="chevron" viewBox="0 0 463 56" preserveAspectRatio="none">
    <polygon points="0,56 243,0 463,56" fill="var(--navy)"/>
    <polygon points="0,56 243,12 463,56" fill="#fff"/>
  </svg>
  <div class="footer footer--fax">
    <div style="text-align:right">7385 Brindle Hollow Lane<br>Fairmont, OR 97402-2049</div>
    <span class="divider"></span>
    <div>☎ 541.555.0142<br>⎙ 541.555.0187</div>
  </div>
</section>

<section class="sheet sheet--letter">
  <div class="brand">Larkspur Ridge Homes</div>
  <svg class="chevron" viewBox="0 0 463 56" preserveAspectRatio="none">
    <polygon points="0,56 231,0 463,56" fill="var(--navy)"/>
    <polygon points="0,56 231,12 463,56" fill="#fff"/>
  </svg>
  <div class="footer footer--letter">
    ☎ 541.555.0142 &nbsp;⎙ 541.555.0187<br>
    Larkspur Ridge Homes, 7385 Brindle Hollow Lane, Fairmont, OR 97402-2049
  </div>
</section>

<div class="env env--back1">
  <svg class="env__flap" viewBox="0 0 517 72" preserveAspectRatio="none"><polygon points="0,0 517,0 500,72 17,72" fill="#fff" stroke="var(--edge)"/></svg>
  <div class="brand">Larkspur Ridge Homes</div>
</div>
<div class="env env--back2">
  <svg class="env__flap" viewBox="0 0 517 72" preserveAspectRatio="none"><polygon points="0,0 517,0 500,72 17,72" fill="#fff" stroke="var(--edge)"/></svg>
  <div class="brand brand--grey">Larkspur Ridge Homes</div>
</div>
<div class="env env--front">
  <div class="brand">Larkspur Ridge Homes</div>
  <svg class="chevron" viewBox="0 0 517 52" preserveAspectRatio="none">
    <polygon points="0,52 258,0 517,52" fill="var(--navy)"/>
    <polygon points="0,52 258,11 517,52" fill="#fff"/>
  </svg>
  <div class="env__address">7385 Brindle Hollow Lane, Fairmont, OR 97402-2049</div>
</div>

<div class="env env--green">
  <svg class="env__flap" viewBox="0 0 517 72" preserveAspectRatio="none"><polygon points="0,0 517,0 500,72 17,72" fill="var(--green)"/></svg>
  <div class="brand brand--light">Larkspur Ridge Homes</div>
</div>
<div class="env env--blue">
  <svg class="env__flap" viewBox="0 0 517 72" preserveAspectRatio="none"><polygon points="0,0 517,0 500,72 17,72" fill="var(--blue)"/></svg>
  <div class="brand brand--light">Larkspur Ridge Homes</div>
</div>
<div class="env env--white">
  <svg class="env__flap" viewBox="0 0 517 72" preserveAspectRatio="none"><polygon points="0,0 517,0 500,72 17,72" fill="#fff" stroke="var(--edge)"/></svg>
  <div class="brand brand--black">Larkspur Ridge Homes</div>
</div>

</body>
</html>
```